Saffron Lantern Court Business Card

I am looking for a business card desgined for my restaurant. It is an Indian restaurant, we are looking for something thats modern, yet traditional with the indian culture, we are looking for colors that match our logo. The logo is a design of the building with the name of the restaurant. for more information on the restaurant go to www.saffronlanterncourt.example

Industry/Entity Type

Indian Restaurant

Contact Information for Business Card

we are looking for somthing thats modern, yet traditional with the indian culture, we are looking for colors that match our logo. The logo is a design of the building with the name of the restaurant. for more information on the restaurant go to www.saffronlanterncourt.example

Requirements
Must have
• The logo that is attached,
• Name: Harvinder Oberoi,
• address of the restaurant: 7328 West Larkspur Rd, Phoenix, Arizona, 85213
• Phone: (602) 555-0147
• Fax: (602) 555-0193
• Restaurant Catering Banquet
• Website: www.SaffronLanternCourt.example
Nice to have
• wanted to get something that goes with the theme of the restaurant, which is traditional but also keep a very professional and modern touch

```html
<!DOCTYPE html>
<html lang="en">
<head>
<meta charset="utf-8">
<title>Saffron Lantern Court – Business Card</title>
<link rel="stylesheet" href="https://fonts.googleapis.com/css2?family=Source+Sans+3:wght@400;600&display=swap">
<style>
  :root {
    --saffron: #f07427;
    --peach: #f9c891;
    --brand-red: #b3312b;
    --page: #ffffff;
  }
  html, body {
    margin: 0;
    padding: 0;
    width: 1085px;
    height: 1200px;
    overflow: hidden;
    background: var(--page);
  }
  .card-sheet {
    display: block;
    width: 1085px;
    height: 1200px;
  }
  .card-sheet text {
    font-family: "Source Sans 3", "Myriad Pro", Arial, sans-serif;
  }
  .surface { fill: var(--saffron); }
  .accent { fill: var(--peach); }
  .brand-name {
    fill: var(--brand-red);
    font-weight: 600;
    text-anchor: middle;
    letter-spacing: 2px;
  }
  .contact-text {
    fill: var(--peach);
    font-weight: 400;
  }
  .person-name { font-size: 68px; }
  .services { font-size: 37px; }
  .detail { font-size: 38px; }
  .icon { fill: var(--peach); }
  .icon-stroke { fill: none; stroke: var(--saffron); stroke-width: 2; }
  .fax-letter {
    fill: var(--saffron);
    font-size: 16px;
    font-weight: 600;
    text-anchor: middle;
  }
</style>
</head>
<body>
<svg class="card-sheet" viewBox="0 0 970 1072" xmlns="http://www.w3.org/2000/svg" aria-label="Saffron Lantern Court business card, front and back">
  <defs>
    <clipPath id="front-clip">
      <rect x="65" y="0" width="860" height="466" rx="10"/>
    </clipPath>
    <clipPath id="back-clip">
      <rect x="70" y="538" width="862" height="466" rx="10"/>
    </clipPath>
    <filter id="soft-shadow" x="-10%" y="-30%" width="120%" height="160%">
      <feDropShadow dx="2" dy="3" stdDeviation="3" flood-color="#7a2e05" flood-opacity="0.55"/>
    </filter>
  </defs>

  <!-- Front of card -->
  <g class="card-front" clip-path="url(#front-clip)">
    <rect class="surface" x="65" y="0" width="860" height="466"/>
    <circle class="accent" cx="492" cy="225" r="309"/>
    <circle class="surface" cx="492" cy="225" r="216"/>
    <rect class="accent" x="65" y="227" width="860" height="14"/>
    <circle class="accent" cx="492" cy="225" r="184"/>
    <g class="brand-mark">
      <text class="brand-name" x="492" y="190" font-size="56">SAFFRON</text>
      <text class="brand-name" x="492" y="256" font-size="56">LANTERN</text>
      <text class="brand-name" x="492" y="322" font-size="56">COURT</text>
    </g>
  </g>

  <!-- Back of card -->
  <g class="card-back" clip-path="url(#back-clip)">
    <rect class="surface" x="70" y="538" width="862" height="466"/>
    <rect class="accent" x="70" y="567" width="620" height="13"/>
    <circle class="accent" cx="792" cy="660" r="176"/>
    <g class="brand-mark">
      <text class="brand-name" x="790" y="650" font-size="46">SAFFRON</text>
      <text class="brand-name" x="790" y="708" font-size="46">LANTERN</text>
      <text class="brand-name" x="790" y="766" font-size="46">COURT</text>
    </g>
  </g>

  <g class="contact-block" filter="url(#soft-shadow)">
    <text class="contact-text person-name" x="94" y="664">Harvinder Oberoi</text>
    <text class="contact-text services" x="112" y="722">Restaurant Catering Banquet</text>

    <!-- phone -->
    <path class="icon" d="M101 784c-4 0-6 3-6 6 1 9 4 15 9 19l3-3-3-5 2-4-2-4-3-9z"/>
    <text class="contact-text detail" x="123" y="810">(602) 555-0147</text>

    <!-- fax -->
    <rect class="icon" x="381" y="780" width="24" height="24" rx="5"/>
    <text class="fax-letter" x="393" y="798">F</text>
    <text class="contact-text detail" x="432" y="810">(602) 555-0193</text>

    <!-- location -->
    <path class="icon" d="M98 863c-7 0-11 5-11 11 0 8 11 20 11 20s11-12 11-20c0-6-4-11-11-11z"/>
    <circle cx="98" cy="874" r="4" fill="var(--saffron)"/>
    <text class="contact-text detail" x="137" y="892">7328 West Larkspur Rd, Phoenix, Arizona, 85213</text>

    <!-- envelope -->
    <rect class="icon" x="91" y="955" width="26" height="17" rx="1"/>
    <path class="icon-stroke" d="M92 956l12 9 12-9M92 971l9-7M116 971l-9-7"/>
    <text class="contact-text detail" x="150" y="972">www.SaffronLanternCourt.example</text>
  </g>
</svg>
</body>
</html>
```